Silver Heron Holdings, LLC Business Card

We need a logo that will be embossed or printed in a singular light color for Business Cards. Would be interested in seeing a Cypress Tree graphic. Our company name is Silver Heron Holdings, LLC. Business Card layout and graphic should project imagine of confidence, integrity and strength.

```html
<!DOCTYPE html>
<html lang="en">
<head>
<meta charset="utf-8">
<title>Silver Heron Holdings, LLC — Business Card</title>
<link href="https://fonts.googleapis.com/css2?family=Quicksand:wght@400;500;700&display=swap" rel="stylesheet">
<style>
  :root {
    --backdrop: #e4e4e2;
    --card: #f1f1f1;
    --ink: #1d1e20;
    --panel: #2b2d30;
    --panel-edge: #1c1d1f;
    --accent: #29b6f0;
    --panel-text: #e9eaec;
    --muted: #3a3b3d;
  }
  * { margin: 0; padding: 0; box-sizing: border-box; }
  html, body {
    width: 1200px; height: 1000px; overflow: hidden;
    background: var(--backdrop);
    font-family: "Quicksand", sans-serif;
  }
  .business-card {
    position: absolute; left: 180px; top: 260px;
    width: 840px; height: 480px;
    background: linear-gradient(135deg, #f6f6f6 0%, #e9e9e9 100%);
    box-shadow: 0 14px 34px rgba(0,0,0,0.18);
    overflow: hidden;
  }
  .brand {
    position: absolute; left: 70px; top: 132px;
    display: flex; align-items: center; gap: 18px;
  }
  .brand-ring {
    width: 96px; height: 96px; flex: none;
    border: 6px solid var(--ink); border-radius: 50%;
  }
  .brand-name {
    font-weight: 700; font-size: 22px; line-height: 1.25;
    color: var(--ink); width: 190px;
  }
  .identity {
    position: absolute; left: 446px; top: 40px; right: 0;
  }
  .employee-name {
    font-weight: 700; font-size: 42px; letter-spacing: 0.5px;
    color: var(--ink); line-height: 1;
  }
  .designation {
    font-weight: 500; font-size: 19px; color: var(--muted);
    margin-top: 6px;
  }
  .identity-rule {
    height: 3px; background: var(--accent); margin-top: 8px;
  }
  .contact-panel {
    position: absolute; left: 420px; top: 132px; right: 0;
    height: 180px; background: var(--panel);
    border-left: 12px solid var(--panel-edge);
    padding: 38px 0 0 36px;
    list-style: none;
  }
  .contact-item {
    display: flex; align-items: center; gap: 24px;
    color: var(--panel-text); font-size: 22px; letter-spacing: 1px;
    margin-bottom: 14px;
  }
  .contact-icon { width: 20px; height: 20px; flex: none; }
  .footer-band {
    position: absolute; left: 0; right: 0; bottom: 0; height: 62px;
    background: linear-gradient(180deg, #2a2c2f 0%, #3a3c40 100%);
  }
</style>
</head>
<body>
  <article class="business-card">
    <div class="brand">
      <span class="brand-ring"></span>
      <span class="brand-name">Silver Heron Holdings, LLC</span>
    </div>

    <header class="identity">
      <h1 class="employee-name">Employee Name</h1>
      <p class="designation">Designation</p>
      <div class="identity-rule"></div>
    </header>

    <ul class="contact-panel">
      <li class="contact-item">
        <svg class="contact-icon" viewBox="0 0 20 20" aria-hidden="true">
          <rect width="20" height="20" rx="2" fill="var(--accent)"/>
          <path d="M4 10 L10 4.5 L16 10 H14 V15.5 H6 V10 Z" fill="var(--panel)"/>
        </svg>
        <span>Address</span>
      </li>
      <li class="contact-item">
        <svg class="contact-icon" viewBox="0 0 20 20" aria-hidden="true">
          <rect width="20" height="20" rx="2" fill="var(--accent)"/>
          <path d="M4 8 Q10 3 16 8 L14.5 9.5 L12.5 8.5 V7.5 Q10 6.8 7.5 7.5 V8.5 L5.5 9.5 Z" fill="var(--panel)"/>
          <rect x="6" y="10" width="8" height="5" rx="1" fill="var(--panel)"/>
        </svg>
        <span>(123) 456 7890</span>
      </li>
      <li class="contact-item">
        <svg class="contact-icon" viewBox="0 0 20 20" aria-hidden="true">
          <rect width="20" height="20" rx="2" fill="var(--accent)"/>
          <rect x="6.5" y="3.5" width="7" height="13" rx="1.5" fill="var(--panel)"/>
          <rect x="8" y="5.5" width="4" height="7" fill="var(--accent)"/>
        </svg>
        <span>(123) 456 789</span>
      </li>
    </ul>

    <div class="footer-band"></div>
  </article>
</body>
</html>
```